Kestrel Gardenworks Business Card

An eye catching, yet simple business card that includes;

1. our logo
2. office phone - 5083172946
3. email - kestrelgardenworks@mailbrook.com
4. website - www.kestrelgardenworks.com
5. instagram - @kestrelgardenworksnv

```html
<!DOCTYPE html>
<html lang="en">
<head>
<meta charset="utf-8">
<title>Kestrel Gardenworks Business Card</title>
<link href="https://fonts.googleapis.com/css2?family=Poppins:wght@400;600;700&display=swap" rel="stylesheet">
<style>
  :root {
    --stage: #ece8e2;
    --paper: #ffffff;
    --paper-shade: #ececec;
    --ink: #1f1b18;
    --copper: #c47a2e;
    --light-text: #f3f1ee;
    --grass-light: #c9e67a;
    --grass-mid: #8cc63f;
    --grass-deep: #5e9e2c;
  }
  * { margin: 0; padding: 0; box-sizing: border-box; }
  html, body { width: 1200px; height: 917px; overflow: hidden; }
  body {
    background: var(--stage);
    font-family: "Poppins", sans-serif;
    position: relative;
  }
  .card {
    position: absolute;
    left: 250px;
    width: 700px;
    height: 400px;
    overflow: hidden;
    box-shadow: 0 10px 26px rgba(0,0,0,0.18);
  }
  .card--front {
    top: 40px;
    background: linear-gradient(135deg, var(--paper) 0%, var(--paper) 45%, var(--paper-shade) 100%);
  }
  .card--back { top: 477px; }

  .front-shapes { position: absolute; inset: 0; }

  .brand {
    position: absolute;
    left: 70px;
    top: 160px;
    display: flex;
    align-items: center;
    gap: 14px;
  }
  .brand-dot {
    width: 22px; height: 22px;
    border-radius: 50%;
    background: var(--copper);
  }
  .brand-name {
    font-weight: 700;
    font-size: 30px;
    line-height: 1.05;
    color: var(--copper);
  }

  .contact {
    position: absolute;
    right: 40px;
    top: 112px;
    text-align: right;
    color: var(--light-text);
  }
  .contact-name {
    font-weight: 700;
    font-size: 21px;
    color: var(--copper);
    line-height: 1.1;
  }
  .contact-role {
    font-size: 12px;
    margin-bottom: 24px;
  }
  .contact-list { list-style: none; }
  .contact-item {
    display: flex;
    justify-content: flex-end;
    align-items: center;
    gap: 10px;
    font-size: 13px;
    line-height: 1;
    margin-bottom: 12px;
    white-space: nowrap;
  }
  .contact-icon {
    width: 15px; height: 15px;
    border-radius: 3px;
    background: var(--copper);
    display: inline-flex;
    align-items: center;
    justify-content: center;
    flex: none;
  }

  .back-photo {
    position: absolute;
    inset: 0;
    background:
      radial-gradient(ellipse at 80% 30%, var(--grass-light) 0%, transparent 60%),
      linear-gradient(160deg, var(--grass-mid) 0%, var(--grass-light) 50%, var(--grass-deep) 100%);
  }
  .back-band {
    position: absolute;
    top: 0; bottom: 0;
    left: 160px;
    width: 240px;
    background: var(--paper);
    display: flex;
    align-items: center;
    justify-content: center;
  }
  .back-brand {
    transform: rotate(90deg);
    display: flex;
    align-items: center;
    gap: 14px;
    white-space: nowrap;
  }
</style>
</head>
<body>

<section class="card card--front" aria-label="Business card front">
  <svg class="front-shapes" width="700" height="400" viewBox="0 0 700 400">
    <path class="swoosh" fill="var(--copper)"
          d="M412,0 C300,120 285,300 395,400 L700,400 L700,0 Z"/>
    <path class="gap" fill="var(--paper)"
          d="M432,0 C322,120 318,290 440,400 L700,400 L700,0 Z"/>
    <path class="panel" fill="var(--ink)"
          d="M448,0 C338,120 334,290 456,400 L700,400 L700,0 Z"/>
  </svg>

  <div class="brand">
    <span class="brand-dot"></span>
    <div class="brand-name">Kestrel<br>Gardenworks</div>
  </div>

  <div class="contact">
    <div class="contact-name">Noah Bellamy</div>
    <div class="contact-role">Manager</div>
    <ul class="contact-list">
      <li class="contact-item">5083172946
        <span class="contact-icon"><svg width="9" height="9" viewBox="0 0 10 10"><path d="M2,1 L4,1 L4.6,3 L3.5,4 C4,5.3 4.7,6 6,6.5 L7,5.4 L9,6 L9,8 C5,8.5 1.5,5 2,1 Z" fill="#fff"/></svg></span>
      </li>
      <li class="contact-item">kestrelgardenworks@mailbrook.com
        <span class="contact-icon"><svg width="10" height="8" viewBox="0 0 10 8"><rect x="0.5" y="0.5" width="9" height="7" fill="none" stroke="#fff"/><path d="M0.5,0.5 L5,4.5 L9.5,0.5" fill="none" stroke="#fff"/></svg></span>
      </li>
      <li class="contact-item">www.kestrelgardenworks.com
        <span class="contact-icon"><svg width="10" height="10" viewBox="0 0 10 10"><circle cx="5" cy="5" r="4.2" fill="none" stroke="#fff"/><ellipse cx="5" cy="5" rx="1.8" ry="4.2" fill="none" stroke="#fff"/><line x1="0.8" y1="5" x2="9.2" y2="5" stroke="#fff"/></svg></span>
      </li>
      <li class="contact-item">@kestrelgardenworksnv
        <span class="contact-icon"><svg width="8" height="8" viewBox="0 0 8 8"><rect x="0.5" y="0.5" width="7" height="7" fill="#fff"/></svg></span>
      </li>
    </ul>
  </div>
</section>

<section class="card card--back" aria-label="Business card back">
  <div class="back-photo" role="img" aria-label="Close-up photo of fresh green grass blades with dew drops"></div>
  <div class="back-band">
    <div class="back-brand">
      <span class="brand-dot"></span>
      <div class="brand-name">Kestrel<br>Gardenworks</div>
    </div>
  </div>
</section>

</body>
</html>
```